Pitch book for Birchmere Property Partners.

Birchmere Partners is a new real estate investment company focused on multifamily (apartment) investments along the San Francisco Peninsula (in other parts of the world it is also referred to as flats). We need a professional Pitch Book i.e. brochure (digital and print) to raise equity from private investors. Read about “pitch book” on Lexipedia. The profile of the investor is conservative and must qualify as an accredited investor. Think high net worth individuals, CEOs and wealthy retiring couples. The investor that is attracted to real estate invest because it is low risk, produce cash flow and provide solid returns over the long term.

The brochure should convey trust, be highly professional and be clean and crisp. I attach a PowerPoint doc to be used as a copy for the brochure. I also attach a brochure of Halvert Crane – I like the look and feel, think it was designed with InDesign.

We will use the brochure at one-on-one meetings with investors where we will present on a laptop; we also need it in a format so that we can email it, print it and use it to be uploaded as a website.

I prefer the up and down scroll format (like you would do on a Mac) compared to PowerPoint but I am open to suggestions.

The photos I used in the PowerPoint presentation was found on the web, please use your own stock images.

Target Market(s)

High net worth individuals

Industry/Entity Type

Real Estate

Font styles to use
Serif

Requirements
Must have
• See attached Power Point
Nice to have
• See attached HVC brochure, I like the look and feel.
Should not have
• I am open to your ideas.

```html
<!DOCTYPE html>
<html lang="en">
<head>
<meta charset="utf-8">
<title>Birchmere Property Partners — Pitch Book Spread</title>
<link rel="stylesheet" href="https://fonts.googleapis.com/css2?family=EB+Garamond:ital,wght@0,400;0,500;0,600;1,400&display=swap">
<style>
  :root {
    --backdrop: #e3e2e6;
    --paper: #f7f7f8;
    --ink: #5c5c66;
    --accent: #5a4b9e;
    --accent-deep: #4a3d8a;
    --photo-sky: #8d8fb8;
    --photo-mid: #a58cb8;
    --photo-water: #3e4670;
    --photo-glow: #e9c98d;
  }
  * { box-sizing: border-box; margin: 0; padding: 0; }
  html, body { width: 1200px; height: 857px; overflow: hidden; }
  body {
    background: var(--backdrop);
    font-family: "EB Garamond", Garamond, serif;
    color: var(--ink);
    position: relative;
  }
  .spread {
    position: absolute;
    left: 80px; top: 118px;
    width: 1040px; height: 620px;
    background: var(--paper);
    box-shadow: 0 18px 40px rgba(0,0,0,.18);
    overflow: hidden;
  }
  .spread-photo { position: absolute; inset: 0; width: 1040px; height: 620px; }
  .spine {
    position: absolute; left: 505px; top: 0; width: 30px; height: 100%;
    background: linear-gradient(90deg, rgba(0,0,0,0) 0%, rgba(0,0,0,.14) 50%, rgba(0,0,0,0) 100%);
  }
  .mission-band {
    position: absolute; left: 0; top: 140px; width: 470px; height: 90px;
    background: linear-gradient(90deg, rgba(90,75,158,.96), rgba(74,61,138,.9));
    color: #fff; padding: 18px 0 0 48px;
  }
  .mission-title { font-size: 28px; font-weight: 500; letter-spacing: .04em; text-transform: uppercase; line-height: 1; }
  .mission-sub { font-size: 13px; letter-spacing: .12em; text-transform: uppercase; margin-top: 8px; }
  .left-copy { position: absolute; left: 48px; top: 262px; width: 420px; }
  .body-text { font-size: 12.5px; line-height: 1.5; font-style: italic; text-align: justify; }
  .section-title {
    color: var(--accent); font-size: 13px; font-weight: 600;
    letter-spacing: .04em; text-transform: uppercase; margin: 18px 0 6px;
  }
  .right-copy { position: absolute; left: 560px; top: 412px; width: 440px; }
  .invest-title { color: var(--accent); font-size: 13px; font-weight: 600; letter-spacing: .05em; text-transform: uppercase; margin-bottom: 10px; }
  .invest-list { list-style: none; }
  .invest-list li {
    position: relative; padding-left: 20px; font-size: 12.5px; line-height: 1.5;
    font-style: italic; margin-bottom: 6px;
  }
  .invest-list li::before {
    content: ""; position: absolute; left: 2px; top: 6px; width: 7px; height: 7px;
    border: 1.5px solid var(--accent); border-radius: 50%;
  }
  .folio-mark { position: absolute; bottom: 14px; width: 6px; height: 8px; background: #8a8a94; }
  .folio-left { left: 14px; }
  .folio-right { right: 14px; }
</style>
</head>
<body>
  <main class="spread">
    <svg class="spread-photo" viewBox="0 0 1040 620" role="img" aria-label="Photograph of modern waterfront apartment towers at dusk with lit windows, trees and a canal">
      <defs>
        <linearGradient id="photoTone" x1="0" y1="0" x2="0.3" y2="1">
          <stop offset="0" stop-color="var(--photo-sky)"/>
          <stop offset="0.45" stop-color="var(--photo-mid)"/>
          <stop offset="0.7" stop-color="var(--photo-glow)" stop-opacity=".75"/>
          <stop offset="1" stop-color="var(--photo-water)"/>
        </linearGradient>
      </defs>
      <path d="M0 0 H1040 V400 H520 V230 H0 Z" fill="url(#photoTone)"/>
    </svg>
    <div class="spine"></div>

    <section class="mission-band">
      <h1 class="mission-title">Our Mission</h1>
      <p class="mission-sub">— To protect and grow your investment</p>
    </section>

    <section class="left-copy">
      <p class="body-text">Birchmere Partners’ core goal is to identify investments that produce consistent cash flow, have long-term value prospects not currently recognized by the market, and once acquired, increase their operational and managerial efficiencies to maximize cash flow and capital appreciation.</p>
      <h2 class="section-title">Why focus on a specific asset class and geography?</h2>
      <p class="body-text">A focused approach is one of our competitive advantages. With 20 years real estate investment and development experience, Birchmere Partners is a Silicon Valley-based multifamily investment and advisory firm, laser-focused on growing cash flow and lasting value for our clients.</p>
    </section>

    <section class="right-copy">
      <h2 class="invest-title">We invest only:</h2>
      <ul class="invest-list">
        <li>In existing properties - we can evaluate existing expenses and rent rolls with more certainty;</li>
        <li>In select San Francisco and Silicon Valley locations - we know the streets and neighborhoods;</li>
        <li>Using low risk core and core plus investment strategies - to reasonably predict cash flow; and</li>
        <li>For the long-term - your investment is a safe-haven that endures market fluctuations.</li>
      </ul>
    </section>

    <span class="folio-mark folio-left"></span>
    <span class="folio-mark folio-right"></span>
  </main>
</body>
</html>
```